Corvanta Solutions Sales Materials & Look

I am looking for an impactful design to a sales/presentation folder.

On the top of the folder I want the power quotes
Pure Nutrition From Phytoplankton
The World's Original Whole Food
The Best Results In Natural Health History

*picture of powder
Corvanta logo.

The colors and font on the corvanta logo are important to keep in tact even for the power quotes.
I'll leave it up to you how you want to stylize it.

On the back on the bottom (subtle) I want the following
Logo
Unit #5 - 418 Harlow Avenue
Larkfield, Maritime Region
Canada
(506) 555 0174
Plus any other styling you want to consider.

We sell marine phytoplankton powder to other businesses. Marine Phytoplankton is the original vegetable on the planet. It's positioned as a natural medicine for chrohn's and colitis, and fibromyalgia.

I have added the business card design. Please add the following information
Martin Greaves - Founder - CEO
email - mkgreaves@corvanta.example
Phone - (506) 555 0192
Corvanta Solutions Inc
Unit #5 - 418 Harlow Avenue
Larkfield, Maritime Region
E1A 4K7
Canada

```html
<!DOCTYPE html>
<html lang="en">
<head>
<meta charset="utf-8">
<title>Corvanta Solutions – Business Card</title>
<link href="https://fonts.googleapis.com/css2?family=Montserrat:wght@400;500;700;800&display=swap" rel="stylesheet">
<style>
  :root {
    --backdrop: #474747;
    --card: #141414;
    --brand-blue: #25a6df;
    --brand-green: #8cc63f;
    --text-light: #f2f2f2;
  }
  * { box-sizing: border-box; margin: 0; padding: 0; }
  html, body {
    width: 1200px; height: 801px; overflow: hidden;
    background: var(--backdrop);
    font-family: "Montserrat", Arial, sans-serif;
  }
  .sheet {
    position: relative; width: 1200px; height: 801px;
    display: flex; align-items: center; justify-content: center; gap: 40px;
  }
  .card {
    position: relative; width: 520px; height: 298px;
    background: var(--card);
    border-radius: 16px;
    border: 2px solid var(--brand-blue);
    overflow: hidden;
  }

  /* wordmark */
  .wordmark { display: flex; align-items: center; gap: 10px; }
  .wordmark__dot {
    width: 22px; height: 22px; border-radius: 50%;
    background: var(--brand-green);
  }
  .wordmark__name {
    color: var(--brand-blue); font-weight: 800; letter-spacing: 0.5px;
  }

  /* front: contact side */
  .card--front .wordmark { position: absolute; left: 36px; top: 34px; }
  .card--front .wordmark__name { font-size: 34px; }

  .person { position: absolute; left: 36px; top: 122px; }
  .person__name { color: var(--brand-blue); font-weight: 800; font-size: 24px; }
  .person__role { color: var(--text-light); font-weight: 400; font-size: 15px; margin-top: 4px; }

  .divider {
    position: absolute; left: 170px; right: 36px; top: 166px;
    height: 1.5px; background: var(--brand-blue);
  }

  .contact { position: absolute; left: 36px; bottom: 30px; list-style: none; }
  .contact li {
    display: flex; align-items: center; gap: 8px;
    color: var(--text-light); font-size: 14px; line-height: 24px;
  }
  .contact svg { width: 13px; height: 13px; fill: var(--brand-blue); flex: none; }

  .address {
    position: absolute; right: 36px; top: 182px;
    text-align: right; font-style: normal;
    color: var(--text-light); font-size: 13px; line-height: 19px;
  }
  .address__company { color: var(--brand-blue); font-weight: 700; }

  /* back: brand side */
  .card--back { display: flex; align-items: center; justify-content: center; }
  .card--back .wordmark { gap: 16px; }
  .card--back .wordmark__dot { width: 44px; height: 44px; }
  .card--back .wordmark__name { font-size: 64px; }
</style>
</head>
<body>
  <main class="sheet">
    <section class="card card--front" aria-label="Business card, contact side">
      <div class="wordmark">
        <span class="wordmark__dot"></span>
        <span class="wordmark__name">Corvanta</span>
      </div>

      <div class="person">
        <p class="person__name">Martin Greaves</p>
        <p class="person__role">Founder - CEO</p>
      </div>

      <span class="divider"></span>

      <ul class="contact">
        <li>
          <svg viewBox="0 0 24 24" aria-hidden="true"><path d="M6.6 10.8a15.1 15.1 0 0 0 6.6 6.6l2.2-2.2a1 1 0 0 1 1-.25 11.4 11.4 0 0 0 3.6.57 1 1 0 0 1 1 1V20a1 1 0 0 1-1 1A17 17 0 0 1 3 4a1 1 0 0 1 1-1h3.5a1 1 0 0 1 1 1c0 1.25.2 2.45.57 3.6a1 1 0 0 1-.25 1z"/></svg>
          (555) 555 0192
        </li>
        <li>
          <svg viewBox="0 0 24 24" aria-hidden="true"><path d="M2 5h20v14H2zm2 2v.5l8 5 8-5V7z"/></svg>
          mkgreaves@corvanta.example
        </li>
      </ul>

      <address class="address">
        <span class="address__company">Corvanta Solutions Inc</span><br>
        Unit #5 - 418 Harlow Avenue<br>
        Larkfield, Maritime Region<br>
        E1A 4K7 Canada
      </address>
    </section>

    <section class="card card--back" aria-label="Business card, brand side">
      <div class="wordmark">
        <span class="wordmark__dot"></span>
        <span class="wordmark__name">Corvanta</span>
      </div>
    </section>
  </main>
</body>
</html>
```